Tea bag packaging design for KELVIRA

Hello. I am creating a green tea and soybean tea, and I am looking for packaging designs. I will attach some designs I like and our current KELVIRA logo. Feel free to follow the designs or create something of your own.

Package size is 200 (W) x 290(L) mm

The package is a white aluminum package so it can accommodate a wide range of colors. We don't want to pay a ton in printing so 5 colors or less is nice. But we will make exceptions for something more colorful if it's well done.

Target Market(s)

Women and Men in 30s-40s

Industry/Entity Type

food and beverage

Font styles to use
Sans Serif
Other font styles liked:
• red hat is the font of the logo

Requirements
Must have
• clean, simple, but bold design
Nice to have
• images of soybeans and green tea leaves on the package

```html
<!DOCTYPE html>
<html lang="en">
<head>
<meta charset="UTF-8">
<title>KELVIRA Green Tea – Pouch Front</title>
<link href="https://fonts.googleapis.com/css2?family=Jost:wght@600;700&family=Fira+Sans:wght@500;600&display=swap" rel="stylesheet">
<style>
  :root {
    --kraft: #c8a77b;
    --kraft-dark: #b38d63;
    --forest: #13652f;
    --lime: #aec752;
    --lime-ring: #8fb33c;
    --tea-brown: #a0542d;
    --ink: #111111;
    --white: #ffffff;
    --page: #ffffff;
  }
  html, body {
    margin: 0;
    padding: 0;
    width: 1200px;
    height: 849px;
    overflow: hidden;
    background: var(--page);
  }
  .canvas {
    position: relative;
    width: 1200px;
    height: 849px;
  }
  .pouch-front {
    position: absolute;
    left: 361px;
    top: 79px;
    width: 477px;
    height: 691px;
    background: var(--kraft);
    overflow: hidden;
    font-family: "Fira Sans", sans-serif;
  }
  .band-left {
    position: absolute;
    left: 0; top: 0;
    width: 107px; height: 402px;
    background: var(--forest);
  }
  .band-bottom {
    position: absolute;
    left: 0; bottom: 0;
    width: 100%; height: 22px;
    background: var(--forest);
  }
  .band-right {
    position: absolute;
    right: 0; top: 443px;
    width: 26px; height: 248px;
    background: var(--forest);
  }
  .brand-badge {
    position: absolute;
    left: 21px; top: 43px;
    width: 170px; height: 170px;
    border-radius: 50%;
    background: var(--lime);
    box-shadow: 0 0 0 3px var(--lime-ring);
    display: flex;
    align-items: center;
    justify-content: center;
  }
  .brand-name {
    font-family: "Jost", sans-serif;
    font-weight: 700;
    font-size: 25px;
    letter-spacing: 1px;
    color: var(--forest);
  }
  .rule {
    position: absolute;
    left: 219px;
    width: 227px;
    height: 3px;
    background: var(--white);
  }
  .rule-top { top: 23px; }
  .rule-mid { top: 96px; }
  .tagline {
    position: absolute;
    left: 219px;
    margin: 0;
    line-height: 1;
    white-space: nowrap;
  }
  .tag-soft {
    top: 31px;
    font-weight: 600;
    font-size: 23px;
    color: var(--white);
  }
  .tag-strong {
    top: 56px;
    font-weight: 600;
    font-size: 30px;
    color: var(--ink);
  }
  .tag-organic {
    top: 112px;
    font-weight: 500;
    font-size: 34px;
    color: var(--white);
  }
  .art {
    position: absolute;
    display: block;
  }
  .art-teacup { left: 126px; top: 149px; }
  .art-leaves { left: 330px; top: 501px; }
  .product-name {
    position: absolute;
    left: 20px;
    margin: 0;
    font-family: "Jost", sans-serif;
    font-weight: 700;
    color: var(--forest);
    line-height: 1;
    white-space: nowrap;
  }
  .product-green {
    top: 441px;
    font-size: 100px;
    letter-spacing: -6px;
  }
  .product-tea {
    top: 518px;
    font-size: 167px;
    letter-spacing: -5px;
  }
</style>
</head>
<body>
<main class="canvas">
  <section class="pouch-front">
    <div class="band-left"></div>
    <div class="band-right"></div>
    <div class="band-bottom"></div>

    <svg class="art art-teacup" width="332" height="296" role="img" aria-label="Line drawing of a steaming cup of tea on a saucer with fresh green tea leaves">
      <defs>
        <linearGradient id="teacupTone" x1="0" y1="0" x2="0" y2="1">
          <stop offset="0" stop-color="#b38d63"/>
          <stop offset="1" stop-color="#a0542d"/>
        </linearGradient>
      </defs>
      <rect width="332" height="296" rx="24" fill="url(#teacupTone)" fill-opacity="0.55"/>
    </svg>

    <div class="brand-badge">
      <span class="brand-name">KELVIRA</span>
    </div>

    <div class="rule rule-top"></div>
    <p class="tagline tag-soft">Taste Real and Nature</p>
    <p class="tagline tag-strong">Fresh From Farm</p>
    <div class="rule rule-mid"></div>
    <p class="tagline tag-organic">100% ORGANIC</p>

    <h1 class="product-name product-green">GREEN</h1>
    <h1 class="product-name product-tea">TEA</h1>

    <svg class="art art-leaves" width="116" height="150" role="img" aria-label="Outline drawing of a green tea leaf sprig">
      <rect width="116" height="150" rx="20" fill="#13652f" fill-opacity="0.14"/>
    </svg>
  </section>
</main>
</body>
</html>
```